I need a website built for my modeling agency company.

On our website, a user can create a profile and we will submit it to thousands of modeling agents throughout the country.

In many cases, they will receive multiple offers from modeling agencies which allows them to pick and choose the contract that is best for them to launch their modeling career.

Some tag lines to consider using:

"Submit your profile to hundreds of modeling agents instantly!"

"Get found and become a star!"

We are: The Runway Guild.

Our Slogan: The World''s Largest Network of Fashion Models and Agents

What We Do: We are an agency with one of the largest networks of fashion professionals that are looking for new modeling talent. We host professional profiles for aspiring models, professional fashion models seeking work, modeling talent seekers, and top modeling agencies. We connect aspiring models with the top modeling agencies in the United States and abroad.

By submitting your FREE profile, you will be instantly introduced to the industry’s leading modeling agents. Within a few days, you could receive multiple, competing offers from modeling agencies that all want to launch your modeling career. Receiving multiple signing offers puts you in control of deciding which contract best suites you!

Reason: I've seen some good designs, but none that are 100% perfect. These are the ones that I like best so far (to give you some ideas): http://files.pixelvantor.com/img/501132/770214/770214_3391045_501132_image.jpg http://files.pixelvantor.com/img/501132/768531/768531_3397712_501132_image.jpg http://files.pixelvantor.com/img/501132/52817/52817_3394420_501132_image.jpg http://files.pixelvantor.com/img/501132/52817/52817_3389163_501132_image.jpg http://files.pixelvantor.com/img/501132/773906/773906_3390287_501132_image.jpg

Target Market(s)

Aspiring models (mostly female, but some male)

Industry/Entity Type

Modeling Agency

Colors

Designer to choose colors to be used in the design.

Requirements
Nice to have
• Somewhere in the top half of the page, I would like there to be a small form for the visitor to fill out. This form will look as follows:

Title: Instantly contact hundreds of modeling agents who are looking for new talent and could make you a star!
Fields: First Name*, Last Name*, Age, Zip Code, Email Address*, Daytime Phone, Evening Phone, Comments.

Then, there will be a "submit" button to proceed to next step of form. Just below the "submit" button, should be the following verbiage: "You will have the opportunity to upload photo(s) and provide other pertinent information in next step."

```html
<!DOCTYPE html>
<html lang="en">
<head>
<meta charset="utf-8">
<title>The Runway Guild</title>
<link href="https://fonts.googleapis.com/css2?family=Cinzel:wght@400&family=Libre+Baskerville:wght@400;700&family=Open+Sans:wght@400;600;700&family=Roboto:wght@400;500&display=swap" rel="stylesheet">
<style>
:root{
  --pink:#e0258a;
  --pink-dark:#b81a6d;
  --ink:#222;
  --text:#444;
  --muted:#888;
  --rule:#d6d6d6;
  --field:#fff;
  --field-line:#d9d9d9;
  --page:#fcfcfc;
  --hero-a:#f2f1f1;
  --hero-b:#d4d3d4;
}
*{box-sizing:border-box;margin:0;padding:0}
html,body{width:1200px;height:1200px;overflow:hidden;background:#fff}
body{position:relative;font-family:"Open Sans",sans-serif;color:var(--text)}
.abs{position:absolute}
.page{position:absolute;left:254px;top:0;width:693px;height:1200px;background:var(--page)}
.top-line{left:254px;top:0;width:693px;height:2px;background:var(--pink)}
.brand{left:333px;top:16px;display:flex;align-items:center;gap:6px}
.brand-mark{width:9px;height:9px;background:var(--ink)}
.brand-name{font-family:"Libre Baskerville",serif;font-size:13px;color:var(--ink);line-height:1;white-space:nowrap}
.brand-slogan{left:333px;top:38px;font-size:5px;color:var(--muted);white-space:nowrap}
.account{left:767px;top:16px;font-family:"Libre Baskerville",serif;font-size:6.6px;font-weight:700;color:var(--ink);white-space:nowrap}
.nav{left:618px;top:36px;display:flex;gap:10px;font-family:"Libre Baskerville",serif;font-size:6.6px;font-weight:700;color:var(--ink);white-space:nowrap}
.nav span.sep{font-weight:400}
.hero{left:254px;top:57px;width:693px;height:386px;background:linear-gradient(90deg,var(--hero-a),var(--hero-b))}
.hero-photo{left:254px;top:57px;width:346px;height:386px;background:linear-gradient(160deg,#c9926a,#e8c9b3 55%,#f3ece7)}
.headline{left:607px;top:83px;font-family:"Cinzel",serif;font-size:28px;line-height:34px;color:var(--ink);white-space:nowrap}
.headline em{font-style:normal;color:var(--pink)}
.lead{left:608px;top:160px;font-family:"Libre Baskerville",serif;font-size:9px;line-height:14px;color:#555;white-space:nowrap;letter-spacing:-0.1px}
.lead b{color:#444}
.field{position:absolute;background:var(--field);border:1px solid var(--field-line);font-size:7px;color:#666;padding:7px 7px}
.submit{left:605px;top:363px;width:128px;height:25px;background:linear-gradient(var(--pink),var(--pink-dark));color:#fff;font-family:"Libre Baskerville",serif;font-size:10.5px;text-align:center;line-height:25px}
.note{left:606px;top:397px;width:260px;font-size:6.5px;line-height:10px;color:#666}
.sec-title{font-family:"Libre Baskerville",serif;font-size:10px;letter-spacing:.5px;color:var(--ink);white-space:nowrap}
.photo{position:absolute}
.blurb{position:absolute;width:175px;font-size:6.8px;line-height:10.3px;color:#444}
.blurb a{color:#333;font-weight:700;text-decoration:underline}
.rule{height:1px;background:var(--rule)}
.model-name{font-family:"Roboto",sans-serif;font-size:10px;font-weight:500;color:#555}
.model-place{font-family:"Roboto",sans-serif;font-size:7px;color:#888;margin-top:2px}
.model-link{font-family:"Roboto",sans-serif;font-size:7px;font-weight:500;color:#444;text-decoration:underline}
.event-title{position:absolute;left:747px;width:145px;font-size:6.6px;font-weight:700;line-height:11px;color:#333}
.event-date{position:absolute;left:747px;font-size:6.5px;color:#999}
.foot-col{position:absolute;font-size:7px;line-height:10.5px;color:#555}
.social{position:absolute;width:19px;height:19px;border-radius:50%;background:#555}
</style>
</head>
<body>
<div class="page"></div>
<div class="abs top-line"></div>

<header>
  <div class="abs brand"><span class="brand-mark"></span><span class="brand-name">The Runway Guild</span></div>
  <div class="abs brand-slogan">The World's Largest Network of Fashion Models and Agents</div>
  <div class="abs account">My Profile | Register | Sign In</div>
  <nav class="abs nav"><span>HOME</span><span class="sep">|</span><span>MEMBERS</span><span class="sep">|</span><span>NEWS</span><span class="sep">|</span><span>ABOUT</span><span class="sep">|</span><span>CONTACT</span></nav>
</header>

<section>
  <div class="abs hero"></div>
  <div class="abs hero-photo" role="img" aria-label="Portrait of a model with long curly blonde hair"></div>
  <h1 class="abs headline" style="font-weight:400">Get <em>Found</em> and<br>Become a Star!</h1>
  <p class="abs lead">Instantly contact <b>hundreds of modeling agents</b> who<br>are looking for new talent and could <b>make you a star!</b></p>
  <div class="field" style="left:605px;top:199px;width:128px;height:25px">First Name</div>
  <div class="field" style="left:745px;top:199px;width:128px;height:25px">Last Name</div>
  <div class="field" style="left:605px;top:230px;width:60px;height:25px">Age</div>
  <div class="field" style="left:675px;top:230px;width:58px;height:25px">Zip Code</div>
  <div class="field" style="left:745px;top:230px;width:128px;height:25px">Email Address</div>
  <div class="field" style="left:605px;top:261px;width:128px;height:25px">Daytime Phone</div>
  <div class="field" style="left:745px;top:261px;width:128px;height:25px">Evening Time Phone</div>
  <div class="field" style="left:605px;top:292px;width:268px;height:60px">Comments</div>
  <div class="abs submit">Submit Form</div>
  <p class="abs note">You will have the opportunity to upload photo(s) and provide other pertinent information in next step.</p>
</section>

<section>
  <h2 class="abs sec-title" style="left:329px;top:466px;font-weight:400">WHAT WE DO</h2>
  <h2 class="abs sec-title" style="left:514px;top:466px;font-weight:400">FASHION NEWS</h2>
  <h2 class="abs sec-title" style="left:698px;top:466px;font-weight:400">MODEL OF THE MONTH</h2>
  <div class="photo" style="left:329px;top:488px;width:174px;height:97px;background:linear-gradient(135deg,#b9c4cc,#6f7f8c)" role="img" aria-label="Team of fashion professionals working at a table"></div>
  <div class="photo" style="left:514px;top:488px;width:174px;height:97px;background:linear-gradient(90deg,#d9d4cf,#6b5a4c,#cfc8c2)" role="img" aria-label="Models walking the runway in patterned dresses"></div>
  <div class="photo" style="left:698px;top:488px;width:174px;height:97px;background:linear-gradient(120deg,#e6e2de,#a89f96)" role="img" aria-label="Male model in a light suit jacket"></div>
  <p class="blurb" style="left:329px;top:599px">We are an agency with one of the largest networks of fashion professionals that are looking for new modeling talent. We host professional profiles for aspiring models, professional fashion... <a>Read More</a></p>
  <p class="blurb" style="left:513px;top:599px">11/1/2013<br>Lorem ipsum dolor sit amet, consectetur adipisicing elit, sed do eiusmod tempor incididunt ut labore et dolore magna aliqua. <a>Read More</a></p>
  <p class="blurb" style="left:697px;top:599px"><b>Julian Reeve</b> from USA is our model of the month. Lorem ipsum dolor sit amet, consectetur adipisicing elit, sed do eiusmod tempor incididunt ut labore et dolore magna aliqua. <a>Read More</a></p>
  <div class="abs rule" style="left:329px;top:663px;width:543px"></div>
</section>

<section>
  <h2 class="abs sec-title" style="left:0;width:1200px;text-align:center;top:682px;font-weight:400">LATEST MODELS</h2>
  <div class="photo" style="left:329px;top:710px;width:127px;height:127px;background:linear-gradient(140deg,#2a2522,#b89d8a)" role="img" aria-label="Portrait of a dark-haired female model"></div>
  <div class="photo" style="left:467px;top:710px;width:127px;height:127px;background:linear-gradient(140deg,#eeeeee,#2b2f3a)" role="img" aria-label="Male model in a dark shirt"></div>
  <div class="photo" style="left:606px;top:710px;width:127px;height:127px;background:linear-gradient(140deg,#f4f4f4,#1e2430)" role="img" aria-label="Male model in a dark blazer"></div>
  <div class="photo" style="left:745px;top:710px;width:127px;height:127px;background:linear-gradient(140deg,#1c1c1c,#9a9a9a)" role="img" aria-label="Black and white portrait of a female model"></div>
  <div class="abs" style="left:329px;top:847px"><div class="model-name">Lena Marsh</div><div class="model-place">MELBOURNE, AU</div><div class="model-link" style="margin-top:5px">VIEW PROFILE</div></div>
  <div class="abs" style="left:468px;top:847px"><div class="model-name">Cole Harmon</div><div class="model-place">TEXAS, USA</div><div class="model-link" style="margin-top:5px">VIEW PROFILE</div></div>
  <div class="abs" style="left:607px;top:847px"><div class="model-name">Evan Pierce</div><div class="model-place">PARIS, FRANCE</div><div class="model-link" style="margin-top:5px">VIEW PROFILE</div></div>
  <div class="abs" style="left:746px;top:847px"><div class="model-name">Nadia Vale</div><div class="model-place">VENICE, ITALY</div><div class="model-link" style="margin-top:5px">VIEW PROFILE</div></div>
  <div class="abs rule" style="left:329px;top:911px;width:543px"></div>
</section>

<section>
  <div class="photo" style="left:329px;top:931px;width:349px;height:152px;background:linear-gradient(120deg,#5a5550,#c8c3be 60%,#8d8782)" role="img" aria-label="Video still of a male model in a striped shirt"></div>
  <svg class="abs" style="left:329px;top:1080px" width="349" height="36" viewBox="0 0 349 36">
    <rect width="349" height="36" fill="#1b1b1b"/>
    <rect x="0" y="2" width="150" height="4" fill="#444"/>
    <rect x="0" y="2" width="80" height="4" fill="#d12020"/>
    <circle cx="80" cy="4" r="6" fill="#eee"/>
    <path d="M25 15 L36 22 L25 29 Z" fill="#ddd"/>
    <path d="M70 19 h4 l5 -4 v14 l-5 -4 h-4 Z" fill="#ddd"/>
    <text x="100" y="26" font-family="Roboto,sans-serif" font-size="11" fill="#fff">0:00 <tspan fill="#aaa">/ 4:37</tspan></text>
    <rect x="197" y="16" width="13" height="9" fill="#d12020"/>
    <text x="224" y="26" font-family="Roboto,sans-serif" font-size="11" font-weight="500" fill="#ccc">720p</text>
    <rect x="265" y="18" width="16" height="7" fill="#aaa"/>
    <rect x="292" y="16" width="20" height="11" fill="#aaa"/>
    <rect x="322" y="14" width="22" height="16" fill="none" stroke="#aaa" stroke-width="2"/>
  </svg>
  <h2 class="abs sec-title" style="left:698px;top:930px;font-weight:400">MODELING EVENTS</h2>
  <div class="photo" style="left:696px;top:958px;width:41px;height:41px;background:linear-gradient(135deg,#ddd,#333)" role="img" aria-label="Model in sunglasses"></div>
  <div class="event-title" style="top:957px">Lorem ipsum dolor sit amet, consectetur adipiscing elit</div>
  <div class="event-date" style="top:981px">26 May, 2013</div>
  <div class="photo" style="left:696px;top:1010px;width:41px;height:41px;background:linear-gradient(135deg,#eee,#555)" role="img" aria-label="Model seated in a dark dress"></div>
  <div class="event-title" style="top:1009px">Lorem ipsum dolor sit amet, consectetur adipiscing elit</div>
  <div class="event-date" style="top:1033px">26 May, 2013</div>
  <div class="photo" style="left:696px;top:1065px;width:41px;height:41px;background:linear-gradient(135deg,#f0eef0,#6a5a66)" role="img" aria-label="Model in a patterned outfit"></div>
  <div class="event-title" style="top:1064px">Lorem ipsum dolor sit amet, consectetur adipiscing elit</div>
  <div class="event-date" style="top:1088px">26 May, 2013</div>
</section>

<footer>
  <div class="abs rule" style="left:329px;top:1142px;width:543px"></div>
  <div class="abs brand" style="top:1160px;left:329px"><span class="brand-mark" style="background:#777"></span><span class="brand-name" style="color:#777">The Runway Guild</span></div>
  <div class="abs brand-slogan" style="top:1179px;left:329px">The World's Largest Network of Fashion Models and Agents</div>
  <div class="foot-col" style="left:513px;top:1153px">Home<br>About<br>Contact</div>
  <div class="foot-col" style="left:605px;top:1153px">Members<br>Agencies<br>News</div>
  <div class="foot-col" style="left:699px;top:1153px">My Profile<br>Register<br>Login</div>
  <div class="social" style="left:792px;top:1154px"></div>
  <div class="social" style="left:820px;top:1154px"></div>
  <div class="social" style="left:848px;top:1154px"></div>
</footer>
</body>
</html>
```